Recreate 3 website banners to be more professional! www.BrightHarbor.com Banners

Hello, thank you so much for working on this project.

This project is to redo the banners on www.BrightHarbor.com

Here's what I am looking for... [3-5 banners]
(1) I am not sure how it should be different - But, I am looking for a more professional graphic banner using the same TEXT that is currently on banner.
(2) Perhaps it would look more professional if it were a solid color banner that does not have white space.
(3) Target audience is business owners/decision makers.

Other notes:
(1) I really like the picture of the software
(2) The picture of the man is okay
(3) Colors of course should match website/logo
(4) There are no source graphics, so the banner graphics that you see on the website is the only thing available.

Let me know if you have any questions.

```html
<!DOCTYPE html>
<html lang="en">
<head>
<meta charset="UTF-8">
<title>Wondering If… Banner</title>
<link rel="stylesheet" href="https://fonts.googleapis.com/css2?family=Arimo:wght@700&display=swap">
<style>
  :root {
    --wall-glow: #8e1c15;
    --wall-mid: #5a0f0b;
    --wall-dark: #220504;
    --desk-top: #f4f8fa;
    --desk-edge: #dfe9ee;
    --alert-red: #d0101c;
    --alert-blue: #1a98cf;
    --suit-light: #3d5a86;
    --suit-dark: #1c2c4a;
    --text-light: #ffffff;
  }
  * { margin: 0; padding: 0; box-sizing: border-box; }
  html, body {
    width: 1200px;
    height: 472px;
    overflow: hidden;
    background: #ffffff;
  }
  .banner {
    position: relative;
    width: 1200px;
    height: 472px;
    overflow: hidden;
    font-family: "Arimo", Arial, sans-serif;
    background:
      radial-gradient(ellipse 60% 70% at 55% 45%, var(--wall-glow) 0%, var(--wall-mid) 55%, var(--wall-dark) 100%);
  }
  .desk {
    position: absolute;
    left: 0;
    top: 417px;
    width: 1200px;
    height: 55px;
    background: linear-gradient(180deg, var(--desk-edge) 0%, var(--desk-top) 35%, #ffffff 100%);
  }
  .headline {
    position: absolute;
    left: 51px;
    top: 50px;
    font-size: 56px;
    line-height: 1;
    font-weight: 700;
    color: var(--text-light);
    letter-spacing: 0.5px;
  }
  .presenter {
    position: absolute;
    left: 500px;
    top: 32px;
    width: 292px;
    height: 408px;
    border-radius: 120px 120px 20px 20px;
    background: linear-gradient(180deg, #6f6a66 0%, var(--suit-light) 30%, var(--suit-dark) 100%);
    opacity: 0.9;
  }
  .question {
    position: absolute;
    display: flex;
    align-items: center;
    justify-content: center;
    height: 76px;
    font-size: 23px;
    font-weight: 700;
    color: var(--text-light);
    white-space: nowrap;
  }
  .question--red { background: var(--alert-red); }
  .question--blue { background: var(--alert-blue); }
  .q-bob   { left: 73px;  top: 152px; width: 333px; }
  .q-sally { left: 123px; top: 277px; width: 347px; }
  .q-amy   { left: 774px; top: 89px;  width: 398px; }
  .q-john  { left: 812px; top: 246px; width: 331px; }
</style>
</head>
<body>
  <div class="banner">
    <div class="desk"></div>
    <div class="presenter" role="img" aria-label="Photo of a grey-haired manager in a navy suit leaning on a desk"></div>
    <h1 class="headline">WONDERING IF...</h1>
    <div class="question question--red q-bob">Bob is on JobNest.com?</div>
    <div class="question question--blue q-sally">Sally is chatting all day?</div>
    <div class="question question--blue q-amy">Amy is sharing company info?</div>
    <div class="question question--red q-john">John needs more work?</div>
  </div>
</body>
</html>
```